Redesign B2B website

We are redesigning/ restructuring our current website. We provide company feedback surveys. We claim to be market leader in our country.
We like to be seen as a trustworthy, reliable and innovative partner to the top 1500 companies in the netherlands.
We want to be seen as a personal company.
Current website http://www.brivanto.nl does not meet our standards mentioned above.
Added Homepage layout. Please check
Target Market(s)
Large businesses, HR, decisiontakers
Industry/Entity Type
It Company
Requirements
Must have
- -The website is intended to be responsive. please take that into account. (propose plankor.es)
-The design should match our Style colors(will be provided)
- Wireframes are provided. Fonts used are Open Sans and Esteban,. Feel free to change things around.
Nice to have
- We like the design to be "flat", not much 3d effects, or icons.
Minimalist, Wordpress style or Metro style.

```html
<!DOCTYPE html>
<html lang="nl">
<head>
<meta charset="utf-8">
<title>Brivanto – Medewerkers- en klantonderzoek</title>
<link href="https://fonts.googleapis.com/css2?family=Open+Sans:ital,wght@0,400;0,600;0,700;1,400;1,600&family=Esteban&display=swap" rel="stylesheet">
<style>
:root{
  --navy:#0f2a4a;
  --blue:#1a5f96;
  --orange:#f39200;
  --grey-band:#f0f0f0;
  --grey-line:#d9d9d9;
  --text:#555;
  --cream:#fbf3d5;
  --footer:#0d2440;
  --footer-text:#b7c4d4;
}
*{box-sizing:border-box;margin:0;padding:0}
html,body{width:835px;height:1200px;overflow:hidden}
body{font-family:"Open Sans",sans-serif;color:var(--text);background:#fff;font-size:10px}
.wrap{width:760px;margin:0 auto;position:relative}

.site-header{height:80px;position:relative}
.brand{position:absolute;left:0;top:20px;display:flex;align-items:center;gap:8px}
.brand-mark{width:24px;height:24px;border-radius:50%;background:var(--blue)}
.brand-name{font-family:"Esteban",serif;font-size:30px;color:var(--navy);letter-spacing:.5px}
.header-contact{position:absolute;right:0;top:26px;display:flex;align-items:center;gap:8px}
.header-contact .phone{font-weight:700;font-size:15px;color:var(--blue)}
.social{width:20px;height:20px;border-radius:50%;background:var(--orange);flex:none}
.social.blue{background:var(--blue)}

.main-nav{height:34px;background:#fff;border-top:3px solid var(--navy);border-bottom:1px solid var(--grey-line);position:relative}
.main-nav ul{list-style:none;display:flex;gap:18px;padding-top:8px}
.main-nav a{color:var(--navy);font-weight:600;font-size:12px;text-decoration:none}
.main-nav a.active{color:var(--blue)}
.search{position:absolute;right:0;top:5px;display:flex;gap:4px}
.search input{width:118px;height:21px;border:1px solid var(--grey-line);font:10px "Open Sans",sans-serif;padding:0 5px}
.search button{height:21px;padding:0 10px;background:var(--orange);color:#fff;border:0;font:600 10px "Open Sans",sans-serif}

.hero{height:272px;margin-top:6px;position:relative;background:linear-gradient(90deg,#dfe6ea 0%,#f4f5f6 100%)}
.hero-photo{position:absolute;left:0;top:0;width:48%;height:100%;background:linear-gradient(160deg,#4b6b52,#2f4a38)}
.hero-quote{position:absolute;right:34px;top:28px;width:360px;background:rgba(15,42,74,.88);padding:16px 18px;font-family:"Esteban",serif;font-style:italic;color:#fff;font-size:20px;line-height:1.3}
.hero-btn{position:absolute;right:34px;top:176px;background:var(--orange);color:#fff;font-weight:700;font-size:14px;padding:9px 18px;border-radius:3px}
.dots{position:absolute;right:34px;bottom:12px;display:flex;gap:5px}
.dots span{width:8px;height:8px;border-radius:50%;background:#9fb3c6}
.dots span.on{background:var(--blue)}

.intro{display:flex;gap:22px;margin-top:22px}
.intro-card{flex:1;border:1px solid var(--grey-line);height:190px}
.intro-card h2{display:inline-block;background:var(--navy);color:#fff;font-family:"Esteban",serif;font-weight:400;font-size:16px;padding:6px 14px;margin:-1px 0 0 -1px}
.intro-card p{padding:12px 14px 0;font-size:10.5px;line-height:1.6}

.clients{margin-top:24px;background:var(--grey-band);height:112px;display:flex;align-items:center;justify-content:center;gap:18px}
.client-badge{width:62px;height:38px;background:#c9ced4;border-radius:3px}
.client-badge.round{width:40px;height:40px;border-radius:50%}

.stories{display:flex;gap:20px;margin-top:16px;height:214px;overflow:hidden}
.quotes,.tweets{width:235px}
.quote{display:flex;gap:8px;margin-bottom:12px}
.quote-photo{width:38px;height:38px;flex:none;background:linear-gradient(#9aaab8,#6d7f90)}
.quote h3,.tweet h3{font-size:10.5px;color:var(--blue);font-weight:700;line-height:1.3}
.quote time,.tweet time{display:block;font-size:9px;color:#999;margin:1px 0}
.quote p,.tweet p{font-size:9.5px;line-height:1.4}
.team-photo{flex:1;height:190px;background:linear-gradient(180deg,#d9dfe6,#8b9cad)}
.tweet{display:flex;gap:8px;margin-bottom:12px}
.tweet-dot{width:22px;height:22px;border-radius:50%;background:var(--blue);flex:none}

.newsletter{background:var(--cream);height:40px;margin-top:4px}
.newsletter .wrap{display:flex;align-items:center;height:40px;gap:8px}
.newsletter .phone{font-weight:700;font-size:14px;color:var(--navy);margin-right:6px;white-space:nowrap}
.newsletter .label{margin-left:24px;color:var(--navy);font-size:10px;white-space:nowrap}
.newsletter input{flex:1;height:22px;border:1px solid var(--grey-line);padding:0 6px;font:10px "Open Sans",sans-serif}
.newsletter button{height:22px;width:32px;background:var(--orange);border:0;color:#fff;font:700 10px "Open Sans",sans-serif}

.site-footer{background:var(--footer);height:164px;color:var(--footer-text)}
.footer-cols{display:flex;padding-top:16px;height:136px}
.footer-cols section{flex:1}
.footer-cols h4{color:#fff;font-size:12px;font-weight:600;margin-bottom:6px}
.footer-cols ul{list-style:none}
.footer-cols li{font-size:9.5px;line-height:1.55}
.legal{border-top:1px solid #25405f;text-align:center;font-size:9px;padding-top:8px}
</style>
</head>
<body>
<header class="site-header wrap">
  <div class="brand"><span class="brand-mark"></span><span class="brand-name">Brivanto</span></div>
  <div class="header-contact">
    <span class="phone">020-41 62 200 - Contact</span>
    <span class="social"></span><span class="social blue"></span><span class="social"></span><span class="social blue"></span>
  </div>
</header>

<nav class="main-nav wrap">
  <ul>
    <li><a href="#">Producten</a></li>
    <li><a href="#">Oplossingen</a></li>
    <li><a href="#">Branches</a></li>
    <li><a href="#">Kennis</a></li>
    <li><a href="#">Klanten</a></li>
    <li><a class="active" href="#">Over Brivanto</a></li>
  </ul>
  <form class="search"><input type="text" placeholder="Zoeken"><button type="button">Zoeken</button></form>
</nav>

<section class="hero wrap">
  <div class="hero-photo" role="img" aria-label="Presentator voor een schoolbord met schetsen"></div>
  <blockquote class="hero-quote">“Inzicht in de beleving van medewerkers geeft ons noodzakelijke informatie waarop we toekomstige beleidsbeslissingen kunnen baseren”</blockquote>
  <div class="hero-btn">Medewerkersonderzoek</div>
  <div class="dots"><span class="on"></span><span></span><span></span><span></span></div>
</section>

<section class="intro wrap">
  <article class="intro-card"><h2>Wie is Brivanto?</h2><p>Brivanto helpt organisaties hun medewerkers beter te begrijpen. Met heldere onderzoeken en persoonlijke begeleiding maken wij feedback bruikbaar voor directie en HR.</p></article>
  <article class="intro-card"><h2>Wat doen wij?</h2><p>Wij ontwikkelen medewerkers-, klant- en 360 graden onderzoeken. Samen met u vertalen wij de uitkomsten naar concrete acties voor de hele organisatie.</p></article>
  <article class="intro-card"><h2>Wat is het resultaat?</h2><p>Betrokken medewerkers, tevreden klanten en betere prestaties. Onze klanten zien hun resultaten verbeteren door gericht te sturen op wat echt telt.</p></article>
</section>

<section class="clients">
  <span class="client-badge"></span><span class="client-badge round"></span><span class="client-badge round"></span><span class="client-badge"></span><span class="client-badge"></span><span class="client-badge"></span><span class="client-badge"></span><span class="client-badge"></span><span class="client-badge"></span>
</section>

<section class="stories wrap">
  <div class="quotes">
    <div class="quote"><div class="quote-photo" role="img" aria-label="Portret klant"></div><div><h3>Kracht in heldere rapportage</h3><time>12 oktober 2013</time><p>Direct zicht op onze verbeterpunten.</p></div></div>
    <div class="quote"><div class="quote-photo" role="img" aria-label="Portret klant"></div><div><h3>Feedback met een vaste partner</h3><time>3 oktober 2013</time><p>Door de begeleiding snel tot actie.</p></div></div>
    <div class="quote"><div class="quote-photo" role="img" aria-label="Portret klant"></div><div><h3>Medewerkers voelen zich gehoord</h3><time>28 september 2013</time><p>Waardevol voor de hele organisatie.</p></div></div>
  </div>
  <div class="team-photo" role="img" aria-label="Team van collega's in een kantoor"></div>
  <div class="tweets">
    <div class="tweet"><span class="tweet-dot"></span><div><h3>Brivanto by @brivanto</h3><p>Nieuwe whitepaper over betrokkenheid nu online</p><time>2 uur geleden</time></div></div>
    <div class="tweet"><span class="tweet-dot"></span><div><h3>Brivanto by @brivanto</h3><p>Bekijk onze feedbacktips voor managers</p><time>5 uur geleden</time></div></div>
    <div class="tweet"><span class="tweet-dot"></span><div><h3>Brivanto by @brivanto</h3><p>Resultaten benchmark 2013 nu beschikbaar</p><time>1 dag geleden</time></div></div>
  </div>
</section>

<section class="newsletter">
  <div class="wrap">
    <span class="phone">020-41 62 200</span>
    <span class="social"></span><span class="social blue"></span><span class="social"></span>
    <span class="label">Schrijf je in voor onze nieuwsbrief</span>
    <input type="email" placeholder="E-mailadres"><button type="button">Go</button>
  </div>
</section>

<footer class="site-footer">
  <div class="footer-cols wrap">
    <section><h4>Wat doen wij</h4><ul><li>Medewerkersonderzoek</li><li>Klantonderzoek</li><li>360 graden feedback</li><li>Exitonderzoek</li><li>Benchmarking</li><li>Advies en training</li></ul></section>
    <section><h4>Waar kunnen we mee helpen</h4><ul><li>Betrokkenheid verhogen</li><li>Verloop verminderen</li><li>Klanttevredenheid meten</li><li>Leiderschap ontwikkelen</li><li>Verandering begeleiden</li><li>Verzuim terugdringen</li></ul></section>
    <section><h4>Ruime ervaring in</h4><ul><li>Zorg en welzijn</li><li>Financiële dienstverlening</li><li>Overheid</li><li>Onderwijs</li><li>Industrie</li><li>Retail</li></ul></section>
    <section><h4>Meer over ons</h4><ul><li>Over Brivanto</li><li>Werken bij</li><li>Nieuws</li><li>Contact</li><li>Route</li></ul></section>
  </div>
  <div class="legal">© 2013 Brivanto. Medewerkers- en klantonderzoek | Privacy en Disclaimer | Algemene voorwaarden</div>
</footer>
</body>
</html>
```